International Property Consultancy

Detailed Wireframe and info document attached.

Brief Overview:

I need a dynamic and well designed website that is easy to use and understand. It has to be unique and different to generic templates that most websites seem to be these days. PLEASE NO GENERIC TEMPLATES FROM THE INTERNET.

Our business has 10 years experience working on struggling international developments that we then work in-house for to turn around and brings bout success. We stay within a project often for long periods of time until success is achieved. We are unique in our approach and completely different to the standard routes to market for many developments. The site is for developers to see what we have done in regards to previous projects, as such we want to incorporate video into this site with a strong design aesthetic. There will be videos of the past projects we have worked on, which will act as case studies.

I like very simple but punchy websites, that people can navigate and understand very easily. Also a big fan of unique and well thought out design aesthetic.

Initial Site layout thoughts:

1) Homepage:
2) About Us
3) What we've done / Work
This part has the projects we have worked on (France, Portugal, London, Morocco). Each one will have some video content and photo images, but also would be good to have a succinct way to mention what we did and the successes in a clever and punchy way.

4) Contact Us

* This is just a guideline. Would be open to input and creative direction on your own part.

*More details and websites we like can be seen in the brief doc attached.

PLEASE VIEW THE WIREFRAME WORD DOC ATTACHED.

Here there are also some more examples to help:

Here are just a few examples of websites and what I like about them:

- www.velmorit.com (clean, nice geometric design aesthetic, good animation when loading and changing pages well thought out all though also coulee be considered a bit dull and basic after the initial homepage slide)
- https://www.farbridgeloop.net (Clean site, quite clinical, lacks video content and doesn't engage greatly).
- https://quiltmarsh.com (minimal, and like how it mixes the design aesthetic more with video and photo content)

- https://www.theamberotter.com (like the layout of this and how it displays the projects and work section)

- https://drov.com (Good use of video content)

- https://crafthalo.studio (minimal to the point and mixes design with video and animation etc...)

Here is another couple of cool websites that may help give you some direction: https://tidewellgroup.com www.drov.com

Hi there, One of the things I thought would be good on the homepage is to add the logo with a 'digital landscape' before flicking down into a slide with video content of the projects... Just an idea but have posted some pics in the brief. We would get this animated for the site. But if you have better ideas, please do run with them. Thanks,

Target Market(s)

Property developers

Number of Pages Required

4 page

Font styles to use
Other font styles liked:
• Read brief

Requirements
Must have
• Needs to be clean, dynamic and easy to follow on desktop and mobile. We will use it as a kind of portfolio website so will need to embed video of past projects we have worked on.

Read brief in docs.
Nice to have
• Clean
Should not have
• Not be another generic template website.
Not have random property stock photos. (We are not a property agency).

```html
<!DOCTYPE html>
<html lang="en">
<head>
<meta charset="utf-8">
<title>Corvalen — Homepage</title>
<link rel="stylesheet" href="https://fonts.googleapis.com/css2?family=Outfit:wght@400;500&display=swap">
<style>
  :root {
    --backdrop: #fdf4ea;
    --page: #ffffff;
    --brand: #123f52;
    --ink: #1e1e1e;
    --muted: #5a5a5a;
    --grid-soft: #f6d9c8;
    --grid-strong: #e59a78;
    --photo-deep: #1a3566;
    --photo-sky: #4a84a3;
    --play: #1c1c1c;
  }
  * { box-sizing: border-box; margin: 0; padding: 0; }
  html, body {
    width: 1200px; height: 2463px; overflow: hidden;
    background: var(--backdrop);
    font-family: "Outfit", sans-serif;
  }
  .screen {
    position: absolute; left: 62px; width: 1075px;
    background: var(--page); overflow: hidden;
  }
  .screen--landing { top: 67px; height: 1025px; }
  .screen--scrolled { top: 1201px; height: 1170px; }

  .site-header {
    position: absolute; top: 30px; left: 56px; right: 56px;
    display: flex; justify-content: space-between; align-items: center;
  }
  .wordmark-small {
    font-size: 22px; font-weight: 500; color: var(--brand); letter-spacing: -0.2px;
  }
  .site-nav { display: flex; gap: 36px; }
  .site-nav a {
    font-size: 11px; font-weight: 500; color: var(--brand); text-decoration: none;
  }

  .landscape { position: absolute; left: 0; right: 0; }
  .screen--landing .landscape {
    top: 225px; height: 377px;
    background: linear-gradient(180deg, rgba(246,217,200,0) 0%, rgba(246,217,200,0.55) 30%, rgba(246,217,200,0.35) 100%);
  }
  .screen--scrolled .landscape {
    top: 444px; height: 160px;
    background: radial-gradient(ellipse 45% 80% at 40% 100%, rgba(229,154,120,0.45), rgba(229,154,120,0) 70%),
                radial-gradient(ellipse 45% 80% at 68% 100%, rgba(229,154,120,0.4), rgba(229,154,120,0) 70%);
  }

  .hero-wordmark {
    position: absolute; left: 0; right: 0; text-align: center;
    font-size: 80px; font-weight: 500; color: var(--brand); letter-spacing: -1px;
  }
  .screen--landing .hero-wordmark { top: 262px; }
  .screen--scrolled .hero-wordmark { top: 262px; }

  .intro { position: absolute; left: 57px; top: 662px; }
  .intro h1 { font-size: 45px; font-weight: 500; color: var(--ink); letter-spacing: -0.3px; line-height: 1.2; }
  .intro p { margin-top: 8px; font-size: 16px; color: var(--muted); }

  .project-video {
    position: absolute; left: 56px; width: 963px; top: 789px;
    background: linear-gradient(90deg, var(--photo-deep) 0%, #3b6f9e 22%, var(--photo-sky) 50%, #3f6f9a 78%, var(--photo-deep) 100%);
  }
  .screen--landing .project-video { height: 236px; }
  .screen--scrolled .project-video { height: 381px; }

  .play-button {
    position: absolute; left: 50%; top: 271px; transform: translateX(-50%);
    width: 66px; height: 66px;
  }
</style>
</head>
<body>

<section class="screen screen--landing">
  <header class="site-header">
    <span class="wordmark-small">corvalen.</span>
    <nav class="site-nav"><a href="#">About</a><a href="#">Contact</a></nav>
  </header>
  <div class="landscape" role="img" aria-label="Soft peach wireframe digital landscape"></div>
  <div class="hero-wordmark">corvalen.</div>
  <div class="intro">
    <h1>We are Corvalen</h1>
    <p>We fulfill international property developments</p>
  </div>
  <div class="project-video" role="img" aria-label="Upward view of curved blue striped building facades against the sky"></div>
</section>

<section class="screen screen--scrolled">
  <header class="site-header">
    <span class="wordmark-small">corvalen.</span>
    <nav class="site-nav"><a href="#">About</a><a href="#">Contact</a></nav>
  </header>
  <div class="hero-wordmark">corvalen.</div>
  <div class="landscape" role="img" aria-label="Coral wireframe hills forming a digital landscape"></div>
  <div class="intro">
    <h1>We are Corvalen</h1>
    <p>We fulfill international property developments</p>
  </div>
  <div class="project-video" role="img" aria-label="Project video still: curved blue striped building facades">
    <svg class="play-button" viewBox="0 0 66 66" aria-hidden="true">
      <circle cx="33" cy="33" r="32" fill="var(--play)" stroke="#3a3a3a" stroke-width="1"/>
      <path d="M26 22 L45 33 L26 44 Z" fill="#ffffff"/>
    </svg>
  </div>
</section>

</body>
</html>
```